New Business Card Design Project

I need a meaningful new business card. Therefore, the website should convey growth, joy, uniqueness, workout and a bit of luxury.
Color scheme should be petrol, gold and matching colors.

```html
<!DOCTYPE html>
<html lang="en">
<head>
<meta charset="utf-8">
<title>Corewell Studio – Business Card</title>
<link href="https://fonts.googleapis.com/css2?family=Cinzel:wght@400&family=Great+Vibes&display=swap" rel="stylesheet">
<style>
  :root {
    --petrol: #19aa9d;
    --graphite: #58595b;
    --gold: #c9a24a;
    --paper: #ffffff;
    --ink: #4a4a4c;
    --backdrop: #1c1c1c;
  }
  html, body {
    margin: 0;
    padding: 0;
    width: 1200px;
    height: 1015px;
    overflow: hidden;
    background: var(--backdrop);
  }
  .canvas {
    position: relative;
    width: 1200px;
    height: 1015px;
  }
  .card {
    position: absolute;
    left: 240px;
    width: 720px;
    height: 411px;
    background: var(--paper);
    overflow: hidden;
    box-shadow: 0 18px 40px rgba(0,0,0,0.55);
  }
  .card--front { top: 70px; }
  .card--back { top: 534px; }
  .card__swoosh {
    position: absolute;
    inset: 0;
    width: 100%;
    height: 100%;
  }

  /* Front */
  .brand {
    position: absolute;
    left: 340px;
    top: 60px;
    width: 340px;
    text-align: center;
  }
  .brand__art {
    width: 230px;
    height: 180px;
    margin: 0 auto;
    border-radius: 50% 50% 12px 12px;
    background: radial-gradient(circle at 50% 45%, rgba(25,170,157,0.28), rgba(88,89,91,0.10) 70%, rgba(255,255,255,0) 100%);
  }
  .brand__name {
    margin-top: 14px;
    font-family: "Cinzel", serif;
    font-size: 28px;
    letter-spacing: 2px;
    white-space: nowrap;
    color: var(--petrol);
  }
  .brand__rule {
    width: 150px;
    height: 2px;
    margin: 8px auto 0;
    background: var(--gold);
  }

  /* Back */
  .person {
    position: absolute;
    left: 44px;
    top: 40px;
  }
  .person__name {
    font-family: "Great Vibes", cursive;
    font-size: 62px;
    line-height: 1;
    color: var(--petrol);
    white-space: nowrap;
  }
  .person__role {
    margin-top: 6px;
    padding-left: 20px;
    font-family: "Cinzel", serif;
    font-size: 15px;
    letter-spacing: 2px;
    color: var(--ink);
  }
  .person__rule {
    width: 120px;
    height: 2px;
    margin: 8px 0 0 20px;
    background: var(--gold);
  }
  .contact {
    position: absolute;
    left: 60px;
    top: 180px;
    list-style: none;
    margin: 0;
    padding: 0;
  }
  .contact__item {
    display: flex;
    align-items: center;
    gap: 12px;
    height: 30px;
    font-family: "Cinzel", serif;
    font-size: 15px;
    letter-spacing: 1px;
    white-space: nowrap;
    color: var(--ink);
  }
  .contact__icon {
    width: 22px;
    height: 22px;
    flex: none;
  }
  .address {
    position: absolute;
    left: 94px;
    top: 300px;
    font-family: "Cinzel", serif;
    font-style: normal;
    font-size: 15px;
    letter-spacing: 1px;
    line-height: 1.6;
    white-space: nowrap;
    color: var(--ink);
  }
</style>
</head>
<body>
<main class="canvas">

  <section class="card card--front" aria-label="Card front">
    <svg class="card__swoosh" viewBox="0 0 720 411" aria-hidden="true">
      <rect width="720" height="411" fill="var(--petrol)"/>
      <path d="M210 0 C120 130 140 320 290 411 L720 411 L720 0Z" fill="var(--paper)"/>
      <path d="M222 0 C140 130 160 320 306 411 L720 411 L720 0Z" fill="var(--graphite)"/>
      <path d="M250 0 C190 130 220 320 400 411 L720 411 L720 0Z" fill="var(--paper)"/>
      <path d="M262 0 C205 130 240 320 430 411 L720 411 L720 0Z" fill="var(--petrol)"/>
      <path d="M290 0 C240 150 320 360 560 411 L720 411 L720 0Z" fill="var(--paper)"/>
      <path d="M290 0 C240 150 320 360 560 411" fill="none" stroke="var(--gold)" stroke-width="3"/>
    </svg>
    <div class="brand">
      <div class="brand__art" role="img" aria-label="Line illustration of a woman in a pilates stretch on a reformer bar with leaves"></div>
      <div class="brand__name">Corewell Studio</div>
      <div class="brand__rule"></div>
    </div>
  </section>

  <section class="card card--back" aria-label="Card back">
    <svg class="card__swoosh" viewBox="0 0 720 411" aria-hidden="true">
      <g transform="translate(720 411) rotate(180)">
        <rect width="720" height="411" fill="var(--petrol)"/>
        <path d="M210 0 C120 130 140 320 290 411 L720 411 L720 0Z" fill="var(--paper)"/>
        <path d="M222 0 C140 130 160 320 306 411 L720 411 L720 0Z" fill="var(--graphite)"/>
        <path d="M250 0 C190 130 220 320 400 411 L720 411 L720 0Z" fill="var(--paper)"/>
        <path d="M262 0 C205 130 240 320 430 411 L720 411 L720 0Z" fill="var(--petrol)"/>
        <path d="M290 0 C240 150 320 360 560 411 L720 411 L720 0Z" fill="var(--paper)"/>
        <path d="M290 0 C240 150 320 360 560 411" fill="none" stroke="var(--gold)" stroke-width="3"/>
      </g>
    </svg>

    <div class="person">
      <div class="person__name">Adrian Vale</div>
      <div class="person__role">Managing Director</div>
      <div class="person__rule"></div>
    </div>

    <ul class="contact">
      <li class="contact__item">
        <svg class="contact__icon" viewBox="0 0 22 22" aria-hidden="true">
          <circle cx="11" cy="11" r="11" fill="var(--petrol)"/>
          <path d="M7.5 6.5l2 0 1 2.5-1.3 1a6 6 0 0 0 2.8 2.8l1-1.3 2.5 1v2a1.2 1.2 0 0 1-1.3 1.2A8.5 8.5 0 0 1 6.3 7.8 1.2 1.2 0 0 1 7.5 6.5z" fill="#fff"/>
        </svg>
        044-987 654 321
      </li>
      <li class="contact__item">
        <svg class="contact__icon" viewBox="0 0 22 22" aria-hidden="true">
          <circle cx="11" cy="11" r="11" fill="var(--petrol)"/>
          <rect x="5.5" y="7" width="11" height="8" fill="none" stroke="#fff" stroke-width="1.4"/>
          <path d="M5.5 7l5.5 4.5L16.5 7" fill="none" stroke="#fff" stroke-width="1.4"/>
        </svg>
        hello@corewellstudio.com
      </li>
      <li class="contact__item">
        <svg class="contact__icon" viewBox="0 0 22 22" aria-hidden="true">
          <circle cx="11" cy="11" r="11" fill="var(--petrol)"/>
          <circle cx="11" cy="11" r="5.5" fill="none" stroke="#fff" stroke-width="1.3"/>
          <ellipse cx="11" cy="11" rx="2.3" ry="5.5" fill="none" stroke="#fff" stroke-width="1.1"/>
          <path d="M5.5 11h11" stroke="#fff" stroke-width="1.1"/>
        </svg>
        www.corewellstudio.com
      </li>
    </ul>

    <address class="address">
      18 Linden Row, Harbour Quarter<br>
      45120, Northland
    </address>
  </section>

</main>
</body>
</html>
```